Ironleaf Foundry Business cards

been in business since 1982
do lost wax casting
primary products are police, fire, QRV ect. badges
custom belt buckles, money clips, coins, awards

Target Market(s)

Police, fire, clubs, ect

Industry/Entity Type

Business

Contact Information for Business Card

I want them to blow your socks off

Requirements
Must have
• "our quality is your pride" Logo
Nice to have
• I have a logo but would like it tweaked
• could be 2 sided with smaller pics of our products on the back, uploading more pics.
• check my wbsite for ideas
• ironleafbuckles.example
• I had the Logo redone but am not 100% sure it exacyly the way I want it to look

```html
<!DOCTYPE html>
<html lang="en">
<head>
<meta charset="utf-8">
<title>Ironleaf Foundry Business Card</title>
<link rel="stylesheet" href="https://fonts.googleapis.com/css2?family=Cinzel:wght@400&family=Didact+Gothic&display=swap">
<style>
  :root {
    --backdrop: #1c1c1c;
    --card-white: #ffffff;
    --ink: #111111;
    --foundry-orange: #f26b21;
    --card-black: #050505;
    --text-light: #ffffff;
  }
  * { box-sizing: border-box; margin: 0; padding: 0; }
  html, body {
    width: 1200px; height: 790px; overflow: hidden;
    background: var(--backdrop);
  }
  .canvas {
    width: 1200px; height: 790px;
    display: flex; align-items: center; justify-content: center;
  }
  .business-card {
    width: 1050px; height: 600px;
    display: flex; flex-direction: column;
    background: var(--card-white);
    overflow: hidden;
  }
  .card-top {
    height: 300px;
    display: flex; align-items: center; justify-content: center;
  }
  .brand {
    display: flex; align-items: center; gap: 22px;
  }
  .brand-square {
    width: 30px; height: 30px;
    background: var(--ink);
  }
  .brand-name {
    font-family: "Didact Gothic", sans-serif; font-weight: 400;
    font-size: 64px; letter-spacing: 2px; color: var(--ink);
    line-height: 1;
  }
  .services-band {
    height: 40px; background: var(--foundry-orange);
    display: flex; align-items: center; justify-content: center;
    font-family: "Didact Gothic", sans-serif; font-size: 22px;
    letter-spacing: 1px; color: var(--text-light); text-transform: uppercase;
  }
  .card-bottom {
    flex: 1; background: var(--card-black); color: var(--text-light);
    display: flex; justify-content: space-between;
    padding: 26px 60px 0 50px;
    font-family: "Didact Gothic", sans-serif;
  }
  .contact-name {
    font-family: "Cinzel", serif; font-size: 34px; font-weight: 400;
    line-height: 42px; margin-bottom: 4px;
  }
  .contact-list { list-style: none; }
  .contact-list li {
    display: flex; align-items: center; gap: 14px;
    font-size: 27px; line-height: 38px;
  }
  .contact-list li.gap-before { margin-top: 8px; }
  .contact-icon { width: 22px; height: 22px; fill: var(--text-light); flex: none; }
  .company-block {
    padding-top: 40px; font-size: 26px; line-height: 34px; font-style: normal;
  }
  .company-name { letter-spacing: 0.5px; -webkit-text-stroke: 0.6px var(--text-light); }
</style>
</head>
<body>
<main class="canvas">
  <article class="business-card">
    <header class="card-top">
      <div class="brand">
        <span class="brand-square"></span>
        <span class="brand-name">Ironleaf Foundry</span>
      </div>
    </header>

    <div class="services-band">Custom&nbsp; Buckles - Rings - Badges - Pins - Money Clips - Coins</div>

    <section class="card-bottom">
      <div class="contact">
        <h2 class="contact-name">Dale Harmon</h2>
        <ul class="contact-list">
          <li>
            <svg class="contact-icon" viewBox="0 0 24 24" aria-hidden="true"><path d="M7 1h10a2 2 0 0 1 2 2v18a2 2 0 0 1-2 2H7a2 2 0 0 1-2-2V3a2 2 0 0 1 2-2zm0 3v15h10V4z"/></svg>
            555 014 2298
          </li>
          <li class="gap-before">
            <svg class="contact-icon" viewBox="0 0 24 24" aria-hidden="true"><path d="M2 8c0-3 5-5 10-5s10 2 10 5v2h-5V8c-1-1-3-1.5-5-1.5S8 7 7 8v2H2zM6 12h12l3 9H3z"/></svg>
            1.800.555.0147
          </li>
          <li>
            <svg class="contact-icon" viewBox="0 0 24 24" aria-hidden="true"><path d="M6 2h12v6H6zM2 9h20v9h-4v4H6v-4H2zm6 7v4h8v-4z"/></svg>
            555.010.4471
          </li>
          <li>
            <svg class="contact-icon" viewBox="0 0 24 24" aria-hidden="true"><path d="M2 5h20v14H2zm2 2v.5l8 5.5 8-5.5V7zm0 2.9V17h16V9.9l-8 5.5z"/></svg>
            sales@ironleaffoundry.example
          </li>
        </ul>
      </div>
      <address class="company-block">
        <div class="company-name">Ironleaf Foundry, Inc.</div>
        <div>410 N. Quarry Rd.</div>
        <div>Millbrook, TX 75999</div>
      </address>
    </section>
  </article>
</main>
</body>
</html>
```